Pelunor Mobile phone

Please can you design a box for a mobile phone.
Dimensions so that the phone
and a USB cable can fit into it.

Additional phones have been added model names have been changed to KMV

KMV350 Mobile phone dimensions
1.2 cm thick

11.3 cm x 6.2 cm

KMV400
128mm*64.5mm*9.5mm

KMV500
146mm*72mm*10.5mm

KMV550 Mobile phone dimensions

.09 cm thick
157mm*78mm*9.5mm

Please put the name Pelunor (Gill San font)
I have also supplied the company logo this will not need to be changed.
I have added images of the phones that the packaging is being designed for. . along with this I have added an example of the instructions that will be inside the packaging. 16.04.14

*The packaging must be scalable so that there is packaging for each of the 4 models* 06.06.2014

Target Market(s)

Quivenel Mobile phone Market

Industry/Entity Type

It Company

Font styles to use
Sans Serif
Other font styles liked:
• Gill Sans

Requirements
Must have
• The design must be on a box that will be foldable so it is laid out in one flat sheet.
the font for the word Pelunor must be Gill Sans.

A design for each phone ( different sizes for each phone).

This has been added 09/05/2014 please can you also provide step by step instructions on how to fold the boxes.

```html
<!DOCTYPE html>
<html lang="en">
<head>
<meta charset="utf-8">
<title>Pelunor Phone Box Dieline</title>
<link rel="stylesheet" href="https://fonts.googleapis.com/css2?family=Montserrat:wght@500;600;700&display=swap">
<style>
  :root {
    --backdrop: #000000;
    --board: #f4f4f7;
    --fold-line: #dcdce2;
    --guide-line: #8a8a8a;
    --ink: #141414;
    --ink-soft: #3a3a3a;
    --badge: #8f8f8f;
    --badge-text: #ffffff;
    --mark: #e9c43a;
    --cradle-light: #ffffff;
    --cradle-shade: #dedee3;
  }
  html, body {
    margin: 0;
    padding: 0;
    width: 1200px;
    height: 875px;
    overflow: hidden;
    background: var(--backdrop);
  }
  .dieline {
    display: block;
    width: 1200px;
    height: 875px;
  }
  .guide { stroke: var(--guide-line); stroke-width: 0.6; }
  .panel { fill: var(--board); }
  .fold { stroke: var(--fold-line); stroke-width: 0.8; fill: none; }
  .brand-name {
    font-family: "Montserrat", sans-serif;
    font-weight: 700;
    fill: var(--ink);
  }
  .brand-dot { fill: var(--mark); }
  .tagline {
    font-family: "Montserrat", sans-serif;
    font-weight: 500;
    font-size: 5.6px;
    fill: var(--ink-soft);
  }
  .tagline-strong { font-weight: 600; fill: var(--ink); }
  .model-badge { fill: var(--badge); }
  .model-label {
    font-family: "Montserrat", sans-serif;
    font-weight: 700;
    font-size: 6.2px;
    letter-spacing: 0.3px;
    fill: var(--badge-text);
  }
</style>
</head>
<body>
<svg class="dieline" viewBox="0 0 945 689" preserveAspectRatio="none" xmlns="http://www.w3.org/2000/svg">
  <defs>
    <radialGradient id="product-glow" cx="0.5" cy="0.45" r="0.6">
      <stop offset="0" stop-color="var(--cradle-light)"/>
      <stop offset="0.7" stop-color="#ececf0"/>
      <stop offset="1" stop-color="var(--cradle-shade)"/>
    </radialGradient>
  </defs>

  <g class="guides">
    <line class="guide" x1="153" y1="0" x2="153" y2="689"/>
    <line class="guide" x1="330" y1="0" x2="330" y2="689"/>
    <line class="guide" x1="418" y1="0" x2="418" y2="689"/>
    <line class="guide" x1="596" y1="0" x2="596" y2="689"/>
    <line class="guide" x1="683" y1="0" x2="683" y2="689"/>
    <line class="guide" x1="839" y1="0" x2="839" y2="689"/>
    <line class="guide" x1="37" y1="33" x2="887" y2="33"/>
    <line class="guide" x1="37" y1="110" x2="887" y2="110"/>
    <line class="guide" x1="37" y1="185" x2="887" y2="185"/>
    <line class="guide" x1="37" y1="497" x2="887" y2="497"/>
  </g>

  <g class="sheet">
    <rect class="panel" x="64" y="110" width="89" height="75"/>
    <rect class="panel" x="64" y="497" width="89" height="78"/>
    <rect class="panel" x="64" y="185" width="775" height="312"/>
    <rect class="panel" x="839" y="185" width="48" height="312"/>
    <rect class="panel" x="330" y="110" width="88" height="465"/>
    <rect class="panel" x="596" y="110" width="87" height="465"/>
    <rect class="panel" x="418" y="33" width="178" height="618"/>
    <rect class="panel" x="683" y="135" width="156" height="386"/>
  </g>

  <g class="folds">
    <line class="fold" x1="64" y1="185" x2="887" y2="185"/>
    <line class="fold" x1="64" y1="497" x2="887" y2="497"/>
    <line class="fold" x1="330" y1="110" x2="683" y2="110"/>
    <line class="fold" x1="330" y1="575" x2="683" y2="575"/>
    <line class="fold" x1="153" y1="185" x2="153" y2="497"/>
    <line class="fold" x1="330" y1="110" x2="330" y2="575"/>
    <line class="fold" x1="418" y1="33" x2="418" y2="651"/>
    <line class="fold" x1="596" y1="33" x2="596" y2="651"/>
    <line class="fold" x1="683" y1="135" x2="683" y2="521"/>
    <line class="fold" x1="839" y1="185" x2="839" y2="497"/>
  </g>

  <g class="front-panel">
    <circle class="brand-dot" cx="176" cy="219" r="15"/>
    <text class="brand-name" x="203" y="227" font-size="20">PELUNOR</text>
    <text class="tagline" x="165" y="271">Expert Packging</text>
    <text class="tagline tagline-strong" x="165" y="280">Mobile phone</text>
    <text class="tagline tagline-strong" x="165" y="289">with USB cable</text>
    <rect role="img" aria-label="Phone in a white cradle, tilted, with a green screen" x="168" y="298" width="156" height="144" rx="34" fill="url(#product-glow)"/>
    <path class="model-badge" d="M271.5 467 H330 V486 H271.5 A9.5 9.5 0 0 1 271.5 467 Z"/>
    <text class="model-label" x="268" y="479">MODEL : KMV350</text>
  </g>

  <g class="side-panel">
    <text class="brand-name" font-size="16" transform="translate(380 326) rotate(-90)" text-anchor="middle">PELUNOR</text>
    <circle class="brand-dot" cx="374" cy="393" r="13"/>
  </g>

  <g class="back-panel">
    <circle class="brand-dot" cx="443" cy="219" r="15"/>
    <text class="brand-name" x="470" y="227" font-size="20">PELUNOR</text>
    <text class="tagline" x="431" y="271">Expert Packging</text>
    <text class="tagline tagline-strong" x="431" y="280">Mobile phone</text>
    <text class="tagline tagline-strong" x="431" y="289">with USB cable</text>
    <rect role="img" aria-label="Phone in a white cradle, tilted, with a green screen" x="434" y="298" width="156" height="144" rx="34" fill="url(#product-glow)"/>
  </g>

  <g class="side-panel">
    <text class="brand-name" font-size="16" transform="translate(641 326) rotate(-90)" text-anchor="middle">PELUNOR</text>
    <circle class="brand-dot" cx="635" cy="393" r="13"/>
  </g>
</svg>
</body>
</html>
```